i need a business card design for my family investment company "norvane holdings" based in dubai. its a diverse investment firm focusing on education, hospitality and automotive. the design has to be modern and try to incorporate the logo "E" in the design. details on card as follow

Tariq H Bin Rashoud
Managing Director
tariq@norvane.ae
www.norvane.ae

Harbor park,palmcrest tower, office 1730, dubai
tel. 04 3819025
mobile.050 4172958

Target Market(s)

card used for networking events and investor meetings

Industry/Entity Type

Hospitality

```html
<!DOCTYPE html>
<html lang="en">
<head>
<meta charset="utf-8">
<title>Norvane Holdings – Business Card</title>
<link href="https://fonts.googleapis.com/css2?family=Questrial&family=Montserrat:wght@600&display=swap" rel="stylesheet">
<style>
  :root {
    --backdrop: #d6d6d6;
    --card-blue: #3d72b0;
    --band-white: #ffffff;
    --navy: #1e2d5c;
    --soft-white: #e3ebf6;
    --rule: rgba(255,255,255,0.45);
  }
  * { margin: 0; padding: 0; box-sizing: border-box; }
  html, body {
    width: 1200px; height: 1000px; overflow: hidden;
    background: var(--backdrop);
  }
  body { position: relative; font-family: "Questrial", sans-serif; }

  .card {
    position: absolute; left: 189px;
    width: 822px; height: 470px;
    background: var(--card-blue);
    overflow: hidden;
    box-shadow: 0 2px 6px rgba(0,0,0,0.15);
  }
  .card--front { top: 20px; }
  .card--back { top: 510px; }

  .band {
    position: absolute; left: 0; right: 0;
    background: var(--band-white);
    display: flex; align-items: center; justify-content: center;
  }
  .card--front .band { top: 36px; height: 104px; }
  .card--back .band { top: 172px; height: 132px; }

  .wordmark {
    font-family: "Questrial", sans-serif;
    font-weight: 400;
    color: var(--navy);
    text-align: center;
    line-height: 1;
  }
  .wordmark__name { display: block; }
  .wordmark__sub { display: block; }
  .card--front .wordmark { margin-left: 120px; }
  .card--front .wordmark__name { font-size: 44px; letter-spacing: 6px; }
  .card--front .wordmark__sub { font-size: 17px; letter-spacing: 7px; margin-top: 4px; }
  .card--back .wordmark__name { font-size: 66px; letter-spacing: 12px; }
  .card--back .wordmark__sub { font-size: 24px; letter-spacing: 13px; margin-top: 6px; }

  .person { position: absolute; left: 58px; top: 252px; color: var(--band-white); }
  .person__name { font-family: "Montserrat", sans-serif; font-weight: 600; font-size: 27px; letter-spacing: 0.5px; }
  .person__title { font-size: 20px; color: var(--soft-white); margin-top: 4px; letter-spacing: 0.5px; }

  .contact {
    position: absolute; left: 560px; top: 222px;
    border-left: 1px solid var(--rule);
    padding-left: 16px;
    color: var(--soft-white);
    font-size: 20px; line-height: 27px; letter-spacing: 0.3px;
  }
  .contact__address { margin-bottom: 2px; }
  .contact__row { display: flex; align-items: center; gap: 6px; }
  .contact__icon { width: 18px; height: 18px; flex: none; }
</style>
</head>
<body>

  <section class="card card--front" aria-label="Business card front">
    <div class="band">
      <div class="wordmark">
        <span class="wordmark__name">NORVANE</span>
        <span class="wordmark__sub">HOLDINGS</span>
      </div>
    </div>

    <div class="person">
      <p class="person__name">Tariq H Bin Rashoud</p>
      <p class="person__title">Managing Director</p>
    </div>

    <div class="contact">
      <p class="contact__address">Harbor park, palmcrest tower,<br>office 1730, dubai</p>
      <p class="contact__row">
        <svg class="contact__icon" viewBox="0 0 24 24" aria-hidden="true"><path fill="#fff" d="M6.6 10.8a15 15 0 0 0 6.6 6.6l2.2-2.2a1 1 0 0 1 1-.25 11.4 11.4 0 0 0 3.6.57 1 1 0 0 1 1 1V20a1 1 0 0 1-1 1A17 17 0 0 1 3 4a1 1 0 0 1 1-1h3.5a1 1 0 0 1 1 1c0 1.25.2 2.45.57 3.57a1 1 0 0 1-.25 1z"/></svg>
        : 04 3819025
      </p>
      <p class="contact__row">
        <svg class="contact__icon" viewBox="0 0 24 24" aria-hidden="true"><rect x="7" y="2" width="10" height="20" rx="2" fill="#fff"/><rect x="9" y="5" width="6" height="7" fill="#3d72b0"/></svg>
        : 050 4172958
      </p>
      <p class="contact__row">
        <svg class="contact__icon" viewBox="0 0 24 24" aria-hidden="true"><rect x="2" y="5" width="20" height="14" rx="1" fill="#fff"/><path d="M2 6l10 7 10-7" fill="none" stroke="#3d72b0" stroke-width="1.5"/></svg>
        : tariq@norvane.ae
      </p>
      <p class="contact__row">
        <svg class="contact__icon" viewBox="0 0 24 24" aria-hidden="true"><g fill="none" stroke="#fff" stroke-width="1.5"><circle cx="12" cy="12" r="9.5"/><ellipse cx="12" cy="12" rx="4" ry="9.5"/><path d="M2.5 12h19"/></g></svg>
        : www.norvane.ae
      </p>
    </div>
  </section>

  <section class="card card--back" aria-label="Business card back">
    <div class="band">
      <div class="wordmark">
        <span class="wordmark__name">NORVANE</span>
        <span class="wordmark__sub">HOLDINGS</span>
      </div>
    </div>
  </section>

</body>
</html>
```